Harborline Network Advisors (HNA) Business Card

Front Side, add Company Logo
1.) Harborline Network Advisors
Director of Operations
Delgado, Marco T
(323) 555 0148
782 n Alder Ave Suite 300 PMB2093
Los Angeles, CA 90013
Marco@HarborlineNA.example
www.HarborlineNA.example
2.) Veteran-Owned Business (with Small EGA)

Back Side
- Pictures are ideas of what you can add. The description is what HNA does.
1.) Business Partners:
- Corvalis Business
- KX&L Business
- Tellmora Business
2.) What we do
- Broker of Internet service (partners above)
- Project Management/ Contract Management
- Government Contracts

```html
<!DOCTYPE html>
<html lang="en">
<head>
<meta charset="utf-8">
<title>Harborline Network Advisors – Business Card</title>
<link href="https://fonts.googleapis.com/css2?family=Poppins:wght@400;500;600&display=swap" rel="stylesheet">
<style>
  :root {
    --card: #2a2627;
    --gold: #f6c31c;
    --page: #f2f2f2;
    --white: #ffffff;
    --ink: #231f20;
  }
  * { margin: 0; padding: 0; box-sizing: border-box; }
  html, body { width: 864px; height: 1200px; overflow: hidden; background: var(--page); }
  body { position: relative; font-family: "Poppins", sans-serif; }

  .card { position: absolute; left: 52px; width: 760px; height: 434px; background: var(--card); overflow: hidden; }
  .card--front { top: 126px; }
  .card--back { top: 640px; }
  .card svg.frame { position: absolute; inset: 0; }

  /* front */
  .person { position: absolute; left: 72px; top: 160px; color: var(--gold); }
  .person__name { font-size: 30px; font-weight: 600; line-height: 1.1; }
  .person__title { font-size: 21px; font-weight: 400; line-height: 1.2; }

  .contact { position: absolute; left: 96px; color: var(--gold); font-size: 17px; font-weight: 400; line-height: 1; display: flex; align-items: center; gap: 8px; }
  .contact--web { left: 110px; top: 264px; letter-spacing: 0.8px; }
  .contact--phone { top: 328px; }
  .contact--mail { top: 360px; }
  .contact--address { top: 392px; }
  .contact svg { width: 22px; height: 22px; flex: none; }

  .company-mark { position: absolute; left: 516px; top: 68px; width: 166px; height: 166px; border: 3px solid var(--gold); border-radius: 50%; display: flex; flex-direction: column; align-items: center; justify-content: center; text-align: center; color: var(--gold); font-size: 17px; font-weight: 500; line-height: 1.25; }

  .veteran { position: absolute; left: 437px; top: 355px; color: var(--ink); font-size: 16px; font-weight: 500; letter-spacing: 0.3px; }

  /* back */
  .photo { position: absolute; top: 55px; width: 214px; height: 158px; border: 2px solid var(--gold); }
  .photo--panel { left: 51px; background: linear-gradient(160deg, #e6e6e2 0%, #cfd3cc 45%, #3f8f4f 70%, #d9dad5 100%); }
  .photo--rack { left: 275px; background: linear-gradient(90deg, #1f1f1d 0%, #6b6224 30%, #c9c9c2 55%, #3a3a33 75%, #1d1d1a 100%); }
  .photo--cabling { left: 499px; background: linear-gradient(170deg, #2b2b27 0%, #6f6f6a 40%, #bdbcb4 60%, #7a4e2e 100%); }

  .band-label { position: absolute; top: 246px; color: var(--ink); font-size: 19px; font-weight: 600; line-height: 24px; letter-spacing: 0.4px; }
  .band-label--services { left: 52px; }
  .band-label--partners { right: 44px; }

  .services { position: absolute; left: 72px; top: 300px; list-style: none; color: var(--gold); font-size: 17px; line-height: 1.2; }
  .services li { position: relative; margin-bottom: 12px; }
  .services li::before { content: ""; position: absolute; left: -23px; top: 4px; width: 11px; height: 11px; background: var(--gold); }

  .partner { position: absolute; top: 306px; height: 60px; background: var(--white); display: flex; align-items: center; justify-content: center; text-align: center; color: var(--ink); font-size: 15px; font-weight: 600; line-height: 1.1; }
  .partner--tellmora { left: 342px; width: 140px; }
  .partner--kxl { left: 496px; width: 86px; font-size: 13px; }
  .partner--corvalis { left: 593px; width: 120px; }
</style>
</head>
<body>

<section class="card card--front" aria-label="Card front">
  <svg class="frame" width="760" height="434" viewBox="0 0 760 434">
    <!-- contact bracket -->
    <path d="M72 434 V248 H365 L375 244" fill="none" stroke="var(--gold)" stroke-width="6"/>
    <path d="M62 434 V258" fill="none" stroke="var(--gold)" stroke-width="6"/>
    <path d="M45 434 V300 H62" fill="none" stroke="var(--gold)" stroke-width="6"/>
    <circle cx="55" cy="274" r="16" fill="var(--gold)"/>
    <circle cx="55" cy="274" r="8" fill="none" stroke="var(--card)" stroke-width="2"/>
    <path d="M47 274 H63 M55 266 V282" stroke="var(--card)" stroke-width="1.6"/>
    <!-- veteran band -->
    <path d="M426 350 H760 V376 H413 Z" fill="var(--gold)"/>
    <circle cx="695" cy="363" r="22" fill="#e8e8e6" stroke="var(--gold)" stroke-width="3"/>
  </svg>

  <div class="company-mark" role="img" aria-label="Harborline Network Advisors logo">
    <span>Harborline</span><span>Network</span><span>Advisors</span>
  </div>

  <div class="person">
    <div class="person__name">Delgado, Marco T</div>
    <div class="person__title">Director of Operations</div>
  </div>

  <div class="contact contact--web">www.HarborlineNA.example</div>

  <div class="contact contact--phone">
    <svg viewBox="0 0 22 22"><circle cx="11" cy="11" r="11" fill="var(--gold)"/><path d="M7 6 l2.5 0 l1 3 l-1.5 1 a7 7 0 0 0 3 3 l1-1.5 l3 1 v2.5 a1 1 0 0 1-1 1 A10 10 0 0 1 6 7 a1 1 0 0 1 1-1z" fill="var(--card)"/></svg>
    (323) 555 0148
  </div>
  <div class="contact contact--mail">
    <svg viewBox="0 0 22 22"><circle cx="11" cy="11" r="11" fill="var(--gold)"/><rect x="5.5" y="7.5" width="11" height="7.5" fill="var(--card)"/><path d="M5.5 7.5 L11 12 L16.5 7.5" fill="none" stroke="var(--gold)" stroke-width="1.2"/></svg>
    Marco@HarborlineNA.example
  </div>
  <div class="contact contact--address">
    <svg viewBox="0 0 22 22"><circle cx="11" cy="11" r="11" fill="var(--gold)"/><path d="M11 17 C7 12 7 10.5 7 9.5 a4 4 0 0 1 8 0 c0 1 0 2.5-4 7.5z" fill="var(--card)"/><circle cx="11" cy="9.5" r="1.6" fill="var(--gold)"/></svg>
    782 n Alder Ave Suite 300 PMB2093, Los Angeles, CA 90013
  </div>

  <div class="veteran">Veteran-Owned Business</div>
</section>

<section class="card card--back" aria-label="Card back">
  <div class="photo photo--panel" role="img" aria-label="Photo of a fibre patch panel with green connectors"></div>
  <div class="photo photo--rack" role="img" aria-label="Photo of a server room aisle with cabled racks"></div>
  <div class="photo photo--cabling" role="img" aria-label="Photo of bundled network cabling in an equipment cabinet"></div>

  <svg class="frame" width="760" height="434" viewBox="0 0 760 434">
    <rect x="0" y="245" width="760" height="25" fill="var(--gold)"/>
    <path d="M55 270 V434" stroke="var(--gold)" stroke-width="3"/>
  </svg>

  <div class="band-label band-label--services">WHAT WE DO</div>
  <div class="band-label band-label--partners">BUSINESS PARTNERS</div>

  <ul class="services">
    <li>Broker of Internet service<br>(partners above)</li>
    <li>Project Management/<br>Contract Management</li>
    <li>Government Contracts</li>
  </ul>

  <div class="partner partner--tellmora">Tellmora Business</div>
  <div class="partner partner--kxl">KX&amp;L<br>Business</div>
  <div class="partner partner--corvalis">Corvalis<br>Business</div>
</section>

</body>
</html>
```